Business card for Internet Marketing Consultant

Simple - need a nice business card design using the logo elements and colors. Keywords: Progressive, professional, stylish, minimalist. Please use the bc as part of the design.

Info for card:

Gareth Pennick
Internet Marketing Strategist
Phone: (520) 318-6047
Email: gareth@brightcanopy.com
Address: 2915 W. Larkmoor Ave., Ste. 118
Tucson, Arizona 85293

Website: www.brightcanopy.com

Industry/Entity Type

Business

Font styles to use
Sans Serif

```html
<!DOCTYPE html>
<html lang="en">
<head>
<meta charset="utf-8">
<title>Bright Canopy – Business Card</title>
<link rel="stylesheet" href="https://fonts.googleapis.com/css2?family=Lato:wght@400;700;900&display=swap">
<style>
  :root {
    --brand-blue: #306bb4;
    --brand-green: #62b45f;
    --ink-grey: #7a7a7a;
    --mark-grey: #c9c9c9;
    --paper: #ffffff;
    --backdrop: #e7e4e1;
  }
  * { box-sizing: border-box; margin: 0; padding: 0; }
  html, body { width: 1200px; height: 1000px; overflow: hidden; }
  body {
    background: var(--backdrop);
    font-family: "Lato", Arial, sans-serif;
    display: flex;
    flex-direction: column;
    align-items: center;
    justify-content: center;
    gap: 60px;
  }
  .card {
    position: relative;
    width: 700px;
    height: 400px;
    overflow: hidden;
    box-shadow: 0 4px 14px rgba(0,0,0,.12);
  }

  /* Front */
  .card-front {
    background: var(--brand-blue);
    display: flex;
    align-items: center;
    justify-content: center;
  }
  .front-mark {
    display: flex;
    align-items: center;
    gap: 18px;
    color: var(--paper);
    font-weight: 900;
    font-size: 64px;
    letter-spacing: -1px;
  }
  .front-mark .mark-square {
    width: 30px; height: 30px;
    background: var(--paper);
  }

  /* Back */
  .card-back { background: var(--paper); }
  .back-monogram {
    position: absolute;
    top: 40px; right: 44px;
    font-weight: 900;
    font-size: 150px;
    line-height: 1;
    color: var(--mark-grey);
  }
  .brand-lockup {
    position: absolute;
    top: 112px; left: 48px;
  }
  .brand-name {
    display: flex;
    align-items: center;
    gap: 10px;
    font-weight: 900;
    font-size: 40px;
    color: var(--brand-blue);
    line-height: 1;
  }
  .brand-name .mark-square {
    width: 18px; height: 18px;
    background: var(--brand-green);
  }
  .brand-tagline {
    margin-top: 6px;
    margin-left: 28px;
    font-size: 13px;
    letter-spacing: 4.2px;
    color: var(--ink-grey);
  }
  .person {
    position: absolute;
    top: 200px; left: 76px;
  }
  .person-name {
    font-weight: 700;
    font-size: 19px;
    color: var(--brand-blue);
  }
  .person-title {
    font-size: 15px;
    color: var(--ink-grey);
    margin-top: 2px;
  }
  .contact-list {
    list-style: none;
    margin-top: 16px;
    font-size: 13px;
    color: var(--ink-grey);
  }
  .contact-list li {
    display: flex;
    align-items: center;
    gap: 10px;
    height: 20px;
  }
  .contact-list svg { width: 12px; height: 12px; fill: var(--brand-green); }
  .edge-bands {
    position: absolute;
    left: 0; bottom: 0;
    width: 700px; height: 90px;
  }
</style>
</head>
<body>

  <section class="card card-front" aria-label="Card front">
    <div class="front-mark"><span class="mark-square"></span>brightcanopy</div>
  </section>

  <section class="card card-back" aria-label="Card back">
    <div class="back-monogram">bc</div>

    <div class="brand-lockup">
      <div class="brand-name"><span class="mark-square"></span>brightcanopy</div>
      <div class="brand-tagline">INTERNET MARKETING STRATEGIES</div>
    </div>

    <div class="person">
      <div class="person-name">Gareth Pennick</div>
      <div class="person-title">President</div>
      <ul class="contact-list">
        <li><svg viewBox="0 0 12 12"><path d="M2.5 0.5l2 2.3-1 1.2a7 7 0 0 0 4.5 4.5l1.2-1 2.3 2-1.3 2A9.5 9.5 0 0 1 0.5 1.8z"/></svg>(520) 318-6047</li>
        <li><svg viewBox="0 0 12 12"><rect x="3" y="0.5" width="6" height="3.5"/><rect x="0.5" y="4.5" width="11" height="5" rx="1"/><rect x="3" y="8" width="6" height="3.5"/></svg>(520) 318-6048</li>
        <li><svg viewBox="0 0 12 12"><path d="M0.5 2h11v8h-11z M1.2 2.6l4.8 4 4.8-4" stroke="#fff" stroke-width="0.8"/></svg>gareth@brightcanopy.com</li>
        <li><svg viewBox="0 0 12 12"><circle cx="6" cy="6" r="5.5"/></svg>www.brightcanopy.com</li>
      </ul>
    </div>

    <svg class="edge-bands" viewBox="0 0 700 90" aria-hidden="true">
      <rect class="band-green" x="470" y="22" width="230" height="8" fill="var(--brand-green)"/>
      <path class="band-blue" d="M0 70 H400 V52 Q400 30 422 30 H700 V90 H0 Z" fill="var(--brand-blue)"/>
    </svg>
  </section>

</body>
</html>
```